I desire to create new signs to be used for general promotion (truck sides, billboards, contract backgrounds)

The center of the sign must be our existing logo, with extensions from that logo to our product types.

Center Logo: VoltNest
surrounding extensions: Electrical Service, Solar Power, EV Charger, and Energy Monitor (each with a descriptive image)
(see attached draft for concept)

Below the image must be an option for one of the following:
318-455-2093 lic 532918
or
517-364-8820 lic 532918

Target Market(s)

homeowners, families, casual commercial

Industry/Entity Type

Electrical

Requirements
Must have
• Must communicate concept completely by image, words are just for clarity.
Should not have
• I like cartoon type images, but not goofy.
Limit number of colors. Bright colors are better.

```html
<!DOCTYPE html>
<html lang="en">
<head>
<meta charset="utf-8">
<title>VoltNest Energy Solutions – Banner Sizes</title>
<link rel="stylesheet" href="https://fonts.googleapis.com/css2?family=Open+Sans:wght@400;600;700;800&display=swap">
<style>
  :root {
    --navy: #0b5485;
    --navy-deep: #063e66;
    --blue-mid: #1f74b0;
    --sky-light: #ffffff;
    --sky: #cfe0fb;
    --sky-edge: #a9c6f2;
    --gold: #f5a623;
    --gold-dark: #c98a1a;
    --cloud: #ffffff;
    --cloud-shade: #d9e6fa;
    --caption: #111111;
    --page: #ffffff;
  }
  * { box-sizing: border-box; margin: 0; padding: 0; }
  html, body { width: 1200px; height: 1200px; overflow: hidden; background: var(--page); }
  body { position: relative; font-family: "Open Sans", Arial, sans-serif; }

  .banner {
    position: absolute;
    overflow: hidden;
    background: radial-gradient(ellipse 55% 75% at 48% 38%, var(--sky-light) 0%, var(--sky) 60%, var(--sky-edge) 100%);
    box-shadow: 0 2px 8px rgba(0,0,0,.35);
  }
  .banner--12x5 { left: 36px; top: 56px; width: 1044px; height: 436px; --u: 4.36px; }
  .banner--13x6 { left: 36px; top: 586px; width: 1130px; height: 520px; --u: 5.2px; }

  .size-caption {
    position: absolute; left: 36px;
    font-size: 19px; color: var(--caption); font-family: Arial, sans-serif;
  }
  .size-caption--12x5 { top: 512px; }
  .size-caption--13x6 { top: 1130px; }

  /* service badges */
  .service {
    position: absolute;
    width: calc(var(--u) * 28.6); height: calc(var(--u) * 28.6);
    transform: translate(-50%, -50%);
  }
  .service__ring {
    position: absolute; inset: 0; border-radius: 50%;
    background: linear-gradient(160deg, var(--gold) 0%, var(--gold-dark) 100%);
    box-shadow: 0 calc(var(--u) * 0.6) calc(var(--u) * 1) rgba(0,0,0,.25);
  }
  .service__disc {
    position: absolute; inset: calc(var(--u) * 1.1); border-radius: 50%;
    background: radial-gradient(circle at 50% 40%, var(--blue-mid) 0%, var(--navy) 55%, var(--navy-deep) 100%);
  }
  .service__icon {
    position: absolute; left: 50%; top: 20%;
    width: 44%; height: 38%; transform: translateX(-50%);
    border-radius: calc(var(--u) * 1.5);
    background: linear-gradient(180deg, #ffffff 0%, #d4e4f5 100%);
    opacity: .9;
  }
  .service--stacked .service__icon { top: 30%; height: 36%; }
  .service__label {
    position: absolute; left: 0; right: 0;
    text-align: center; color: #fff; font-weight: 700;
    font-size: calc(var(--u) * 2.8); line-height: 1.1;
  }
  .service__label--bottom { top: 65%; }
  .service__label--top { top: 14%; }
  .service__label--foot { top: 77%; }
  .service__shadow {
    position: absolute; left: 15%; right: 15%; top: 108%;
    height: calc(var(--u) * 1.4); border-radius: 50%;
    background: rgba(70,90,120,.35); filter: blur(2px);
  }

  .service--electrical { left: 15%; top: 23.4%; }
  .service--monitoring { left: 15%; top: 55.6%; }
  .service--solar { left: 85.2%; top: 21%; }
  .service--ev { left: 85.2%; top: 56%; }

  /* centre brand */
  .brand {
    position: absolute; left: 48.3%; top: 68%;
    transform: translate(-50%, -50%);
    font-weight: 700; color: var(--navy);
    font-size: calc(var(--u) * 20); letter-spacing: -0.02em; line-height: 1;
    white-space: nowrap;
  }
  .brand-dot {
    position: absolute; left: 48.3%; top: 34%;
    width: calc(var(--u) * 20); height: calc(var(--u) * 20);
    transform: translate(-50%, -50%); border-radius: 50%;
    background: var(--gold);
  }

  /* corner cloud panels */
  .cloud-panel {
    position: absolute; bottom: 0;
    background: var(--cloud);
    border: calc(var(--u) * 1.6) solid var(--navy);
    border-bottom: none;
  }
  .cloud-panel--left {
    left: calc(var(--u) * -2); width: 34%; height: 25%;
    border-left: none;
    border-radius: 0 calc(var(--u) * 14) 0 0;
  }
  .cloud-panel--right {
    right: calc(var(--u) * -2); width: 34%; height: 28%;
    border-right: none;
    border-radius: calc(var(--u) * 16) 0 0 0;
  }
  .cloud-accent {
    position: absolute; border-radius: 50%;
    width: calc(var(--u) * 10); height: calc(var(--u) * 10);
    background: var(--gold);
  }
  .cloud-accent--left { left: 1.5%; bottom: 16%; }
  .cloud-accent--right { right: 1.5%; bottom: 22%; }

  .web-address {
    position: absolute; left: 2.6%; bottom: 3.2%;
    color: var(--navy); font-weight: 800;
    font-size: calc(var(--u) * 5.4); white-space: nowrap;
  }
  .contact-line {
    position: absolute; right: 1.6%; bottom: 4%;
    color: var(--navy); font-weight: 700;
    font-size: calc(var(--u) * 4.3); white-space: nowrap; letter-spacing: .02em;
  }
</style>
</head>
<body>

<section class="banner banner--12x5" aria-label="VoltNest banner, 12 by 5 feet">
  <div class="service service--electrical">
    <div class="service__ring"></div><div class="service__disc"></div>
    <div class="service__icon" role="img" aria-label="Light bulb icon"></div>
    <p class="service__label service__label--bottom">Electrical<br>Service</p>
    <div class="service__shadow"></div>
  </div>
  <div class="service service--monitoring service--stacked">
    <div class="service__ring"></div><div class="service__disc"></div>
    <p class="service__label service__label--top">Monitoring</p>
    <div class="service__icon" role="img" aria-label="Rising chart with gears icon"></div>
    <p class="service__label service__label--foot">Automation</p>
    <div class="service__shadow"></div>
  </div>
  <div class="service service--solar">
    <div class="service__ring"></div><div class="service__disc"></div>
    <div class="service__icon" role="img" aria-label="Solar panel with sun icon"></div>
    <p class="service__label service__label--bottom">Solar Power</p>
    <div class="service__shadow"></div>
  </div>
  <div class="service service--ev">
    <div class="service__ring"></div><div class="service__disc"></div>
    <div class="service__icon" role="img" aria-label="Car at charging station icon"></div>
    <p class="service__label service__label--bottom">ev Chargers</p>
    <div class="service__shadow"></div>
  </div>

  <div class="brand-dot"></div>
  <h1 class="brand">VoltNest</h1>

  <div class="cloud-accent cloud-accent--left"></div>
  <div class="cloud-accent cloud-accent--right"></div>
  <div class="cloud-panel cloud-panel--left"></div>
  <div class="cloud-panel cloud-panel--right"></div>
  <p class="web-address">VoltNestEnergy.com</p>
  <p class="contact-line">318-455-2093 lic 532918</p>
</section>
<p class="size-caption size-caption--12x5">12 feet W x 5 feet H</p>

<section class="banner banner--13x6" aria-label="VoltNest banner, 13 by 6 feet">
  <div class="service service--electrical">
    <div class="service__ring"></div><div class="service__disc"></div>
    <div class="service__icon" role="img" aria-label="Light bulb icon"></div>
    <p class="service__label service__label--bottom">Electrical<br>Service</p>
    <div class="service__shadow"></div>
  </div>
  <div class="service service--monitoring service--stacked">
    <div class="service__ring"></div><div class="service__disc"></div>
    <p class="service__label service__label--top">Monitoring</p>
    <div class="service__icon" role="img" aria-label="Rising chart with gears icon"></div>
    <p class="service__label service__label--foot">Automation</p>
    <div class="service__shadow"></div>
  </div>
  <div class="service service--solar">
    <div class="service__ring"></div><div class="service__disc"></div>
    <div class="service__icon" role="img" aria-label="Solar panel with sun icon"></div>
    <p class="service__label service__label--bottom">Solar Power</p>
    <div class="service__shadow"></div>
  </div>
  <div class="service service--ev">
    <div class="service__ring"></div><div class="service__disc"></div>
    <div class="service__icon" role="img" aria-label="Car at charging station icon"></div>
    <p class="service__label service__label--bottom">ev Chargers</p>
    <div class="service__shadow"></div>
  </div>

  <div class="brand-dot"></div>
  <h2 class="brand">VoltNest</h2>

  <div class="cloud-accent cloud-accent--left"></div>
  <div class="cloud-accent cloud-accent--right"></div>
  <div class="cloud-panel cloud-panel--left"></div>
  <div class="cloud-panel cloud-panel--right"></div>
  <p class="web-address">VoltNestEnergy.com</p>
  <p class="contact-line">318-455-2093 lic 532918</p>
</section>
<p class="size-caption size-caption--13x6">13 feet W x 6 feet H</p>

</body>
</html>
```